Driving-coach/trainer who wants to inform about the offer and how I can help people to drive more re

I need a flyer that informs potential customers about my offer.

DL size 210 mm x 99 mm, vertical!

I'm a trainer/coach who helps people to drive a car more relaxed, without fear and more confident.

It's a one to one training. I do train people in their own car. It gets people their freedom back to go where and when they like to go by own car...
Updates

Project Deadline Extended Reason: I would like to extend my project... didn't find the time to give feedback because of unexpected other jobs I had to do.Would be great if you could extend my project around 5 more days. THANKS. Added Wednesday, January 4, 2017

Target Market(s)

People (man an woman) who are afraid of driving a car, or are very stressed while driving....

Industry/Entity Type

Life Coaching

Font styles to use
Sans Serif

Colors
acd136

Requirements
Must have
• Page 1:
• -my offer (see text-pdf)
• -three fotos (see attached files "Pixavine") of people who are satisfied with my offer
• Page 2:
• -advantages in the work with me.
• -contact information
• -and a picture of me (see attached file) next to the contact information or the advantages of my work
• -my logo (see attached file) on Page 1 + 2
• -i like a "clear" and structured layout. "Less is more"

```html
<!DOCTYPE html>
<html lang="de">
<head>
<meta charset="utf-8">
<title>Fahrangst Erfolgreich Loswerden – Flyer</title>
<link rel="stylesheet" href="https://fonts.googleapis.com/css2?family=Open+Sans:wght@400;600;700;800&display=swap">
<style>
  :root {
    --backdrop: #1c1c1c;
    --paper: #ffffff;
    --green: #5aad45;
    --green-dark: #3e9a35;
    --grey-text: #5a5a5a;
    --body-text: #3a3a3a;
    --photo-sky: #e9ece4;
    --photo-warm: #d9c4a0;
    --photo-car: #9aa2a8;
  }
  * { margin: 0; padding: 0; box-sizing: border-box; }
  html, body {
    width: 1200px; height: 2308px; overflow: hidden;
    background: var(--backdrop);
    font-family: "Open Sans", Arial, sans-serif;
  }
  .flyer {
    position: absolute; left: 144px; top: 185px;
    width: 912px; height: 1937px;
    background: var(--paper);
    overflow: hidden;
  }
  .headline {
    position: absolute; left: 58px; top: 62px;
    color: var(--green); font-weight: 800;
    font-size: 72px; line-height: 84px; letter-spacing: -0.5px;
  }
  .question {
    position: absolute; left: 58px;
    color: var(--grey-text); font-weight: 400;
    font-size: 52px; line-height: 56px;
  }
  .question--relax { top: 268px; }
  .question--panic { top: 395px; }
  .badge {
    position: absolute; left: 575px; top: 382px;
    width: 266px; height: 264px; border-radius: 50%;
    background: var(--green); color: #fff;
    display: flex; align-items: center; justify-content: center; text-align: center;
    font-weight: 700; font-size: 38px; line-height: 44px;
  }
  .situations-title {
    position: absolute; left: 58px; top: 628px;
    color: var(--green); font-weight: 800;
    font-size: 41px; line-height: 48px;
  }
  .photo {
    position: absolute; left: 0; top: 970px; width: 912px; height: 704px;
    background:
      radial-gradient(ellipse 260px 300px at 640px 340px, var(--photo-warm) 0%, rgba(217,196,160,0) 100%),
      radial-gradient(ellipse 400px 220px at 360px 620px, var(--photo-car) 0%, rgba(154,162,168,0) 100%),
      linear-gradient(180deg, #ffffff 0%, var(--photo-sky) 35%, #d8dccf 100%);
  }
  .situation {
    position: absolute;
    font-size: 26px; line-height: 32.5px; color: var(--body-text);
    white-space: nowrap;
  }
  .situation b { color: var(--green); font-weight: 700; }
  .situation b.dark { color: var(--green-dark); }
  .situation .tick {
    position: absolute; left: -34px; top: 4px; width: 27px; height: 27px;
  }
  .situation--fear   { left: 88px;  top: 740px; }
  .situation--trust  { left: 88px;  top: 1003px; }
  .situation--stress { left: 88px;  top: 1186px; }
  .situation--places { left: 519px; top: 740px; }
  .band {
    position: absolute; left: 0; top: 1674px; width: 912px; height: 70px;
    background: var(--green); color: #fff;
    font-weight: 700; font-size: 36px; line-height: 70px;
    padding-left: 80px;
  }
  .coach-name {
    position: absolute; left: 76px; top: 1772px;
    color: var(--green); font-weight: 400;
    font-size: 58px; line-height: 64px; letter-spacing: 6px;
  }
  .coach-role {
    position: absolute; left: 78px; top: 1844px;
    color: var(--green); font-weight: 400;
    font-size: 40px; line-height: 46px; letter-spacing: 5.5px;
  }
</style>
</head>
<body>
<main class="flyer">
  <h1 class="headline">Fahrangst Erfolgreich<br>Loswerden!</h1>
  <p class="question question--relax">Sie wollen endlich entspannt<br>und sicher Auto fahren?</p>
  <p class="question question--panic">Panikattacken beim<br>Autofahren<br>überwinden?</p>
  <div class="badge">Dann<br>sind Sie<br>hier<br>richtig!</div>

  <h2 class="situations-title">Kommt Ihnen eine<br>dieser Situationen bekannt vor?</h2>

  <div class="photo" role="img" aria-label="Foto: lächelnde junge Frau lehnt aus dem Fenster eines silbernen Autos und zeigt den Daumen nach oben"></div>

  <p class="situation situation--fear">
    <svg class="tick" viewBox="0 0 26 26"><circle cx="13" cy="13" r="11" fill="none" stroke="#3e9a35" stroke-width="2.5"/><path d="M7.5 13.5l4 4 7-8" fill="none" stroke="#3e9a35" stroke-width="2.8" stroke-linecap="round" stroke-linejoin="round"/></svg>
    <b>Angst oder Panikattacken</b><br>begleiten Sie beim<br>Autofahren. Vielleicht<br><b>vermeiden</b> Sie deshalb das<br>Autofahren komplett. - Sie<br>möchten <b>angstfrei und/oder</b><br><b>ohne Panikattacken</b> fahren.
  </p>
  <p class="situation situation--trust">
    <svg class="tick" viewBox="0 0 26 26"><circle cx="13" cy="13" r="11" fill="none" stroke="#3e9a35" stroke-width="2.5"/><path d="M7.5 13.5l4 4 7-8" fill="none" stroke="#3e9a35" stroke-width="2.8" stroke-linecap="round" stroke-linejoin="round"/></svg>
    Sie <b>trauen sich das</b><br><b>Autofahren nicht (mehr) zu.</b><br>- Sie wünschen sich, <b>sicher,</b><br><b>entspannt und stressfrei</b><br><b>Auto zu fahren.</b>
  </p>
  <p class="situation situation--stress">
    <svg class="tick" viewBox="0 0 26 26"><circle cx="13" cy="13" r="11" fill="none" stroke="#3e9a35" stroke-width="2.5"/><path d="M7.5 13.5l4 4 7-8" fill="none" stroke="#3e9a35" stroke-width="2.8" stroke-linecap="round" stroke-linejoin="round"/></svg>
    <b class="dark">Autofahren</b> erleben Sie<br>unter <b class="dark">hoher Anspannung</b><br><b class="dark">und Stress.</b> - Sie<br>wünschen sich,<br>Autofahren <b class="dark">sicher</b><br><b class="dark">und entspannt</b><br>zu erleben.
  </p>
  <p class="situation situation--places">
    <svg class="tick" viewBox="0 0 26 26"><circle cx="13" cy="13" r="11" fill="none" stroke="#3e9a35" stroke-width="2.5"/><path d="M7.5 13.5l4 4 7-8" fill="none" stroke="#3e9a35" stroke-width="2.8" stroke-linecap="round" stroke-linejoin="round"/></svg>
    Bestimmte Situationen (z.B.<br><b>Autobahn, Baustellen,</b><br><b>Stadtvekehr</b>...) bereiten<br>Ihnen <b>großen Stress.</b> - Sie<br>möchten diese Situationen<br><b>souveräner</b> meistern.
  </p>

  <div class="band">Das muss nicht so bleiben!</div>

  <p class="coach-name">Carina Wendler</p>
  <p class="coach-role">Fahrangst–Bewältigungs–Coach</p>
</main>
</body>
</html>
```